Maren's Atelier, Beauty & Therapy. New business in Verbier, Switzerland

Simple Flyer to put in evidence a particular service that the studio offers that is
EMS ( ELECTRIC MUSCLE STIMULATION)
There is a bike festival in Verbier ion the 12th of August and i would like to take an opportunity of this slot to advertise our new suit of EMS that can be very helpful for bike riders. The product is a suit with muscle electrostimulation, And there are many advantages and functionnality. For sportsmen and women, it can
I don't have any particular picture be cause the product is very new.
But i can send you some images for you to understand what it is, but if you find some images on the web it is better :)
I upload different versions of Logo, PLEASE FEEL FREE TO CHOOSE WHAT IS BEST :)
please check this link for more information about the product applied for bikers
https://www.pulsavo-fit.com/en/cycling-training-with-muscle-electrostimulation/
Updates
Hello Designers,
Here are a few details concerning the project;
- Maren's Atelier is not a reseller of the EMS suits, but we provide it as a service inside our studio.
- We wish to communicate on this new technology in order to bring a maximum of attention, not only for the suit, but also for the brand it self, since it is new in Verbier.
- for the flyer, i would like it to be simple, appealing, and without too much text.
- a french version of the same flyer is appreciated, without extra cost ;)
Thanks
Hello all designers,
thank you for all the good work.
For you who mentioned a date for the festival, i suggest please to take it off, and keep only " Alpenrad Pedal Days" if you want.
Thank you

```html
<!DOCTYPE html>
<html lang="en">
<head>
<meta charset="utf-8">
<title>Maren's Atelier – Cycling Training with Muscle Electrostimulation</title>
<link rel="stylesheet" href="https://fonts.googleapis.com/css2?family=Montserrat:wght@500;700;800&display=swap">
<style>
  :root {
    --plum: #6b1657;
    --plum-deep: #5a0f49;
    --magenta: #a3267c;
    --cream: #fbece8;
    --blush: #f7e1dc;
    --ink: #1f1a1d;
  }
  * { margin: 0; padding: 0; box-sizing: border-box; }
  html, body { width: 900px; height: 1200px; overflow: hidden; background: var(--cream); }
  .flyer {
    position: relative;
    width: 900px;
    height: 1200px;
    overflow: hidden;
    background: var(--cream);
    font-family: "Montserrat", Arial, sans-serif;
    color: var(--ink);
  }
  .flyer-shapes { position: absolute; inset: 0; }
  .brand {
    position: absolute;
    left: 40px;
    top: 150px;
    width: 390px;
    display: flex;
    flex-direction: column;
    align-items: center;
    gap: 18px;
  }
  .brand-mark {
    width: 96px; height: 96px;
    border-radius: 50%;
    border: 4px solid var(--plum);
  }
  .brand-name {
    font-weight: 700;
    font-size: 34px;
    letter-spacing: 3px;
    text-transform: uppercase;
    color: var(--plum);
  }
  .headline {
    position: absolute;
    left: 0; right: 0;
    top: 778px;
    text-align: center;
    text-transform: uppercase;
    line-height: 1.05;
  }
  .headline-kicker {
    display: block;
    font-weight: 800;
    font-size: 31px;
    color: var(--magenta);
  }
  .headline-main {
    display: block;
    font-weight: 800;
    font-size: 41px;
    color: var(--plum);
  }
  .headline-rule {
    position: absolute;
    left: 92px; right: 92px;
    top: 880px;
    height: 2px;
    background: var(--plum);
  }
  .body-copy {
    position: absolute;
    left: 60px; right: 60px;
    top: 905px;
    text-align: center;
    font-weight: 500;
    font-size: 20.5px;
    line-height: 1.28;
  }
  .body-copy p + p { margin-top: 26px; }
  .body-copy strong { font-weight: 700; }
</style>
</head>
<body>
<main class="flyer">
  <svg class="flyer-shapes" width="900" height="1200" viewBox="0 0 900 1200">
    <defs>
      <linearGradient id="heroTone" x1="0" y1="0" x2="1" y2="1">
        <stop offset="0" stop-color="#f3b66a"/>
        <stop offset="0.35" stop-color="#c98a55"/>
        <stop offset="0.7" stop-color="#5b4a3a"/>
        <stop offset="1" stop-color="#2f3a2a"/>
      </linearGradient>
      <linearGradient id="studioTone" x1="0" y1="0" x2="0" y2="1">
        <stop offset="0" stop-color="#eeeeee"/>
        <stop offset="1" stop-color="#c9c9c9"/>
      </linearGradient>
      <linearGradient id="parkTone" x1="0" y1="0" x2="0" y2="1">
        <stop offset="0" stop-color="#8fb8e0"/>
        <stop offset="0.45" stop-color="#5f8a4c"/>
        <stop offset="1" stop-color="#7aa95a"/>
      </linearGradient>
      <clipPath id="studioClip"><circle cx="243" cy="610" r="152"/></clipPath>
      <clipPath id="parkClip"><circle cx="530" cy="622" r="128"/></clipPath>
    </defs>

    <rect class="hero-photo" x="0" y="0" width="900" height="760" fill="url(#heroTone)"
          role="img" aria-label="Smiling cyclist in helmet and sunglasses carrying a red road bike at sunset by a river"/>

    <path class="swoosh-left" d="M0 400 C 80 440, 140 470, 170 530 L 170 760 L 0 760 Z" fill="var(--plum)"/>
    <path class="swoosh-right" d="M900 430 C 790 560, 680 640, 520 690 L 900 760 Z" fill="var(--magenta)"/>
    <path class="swoosh-right-deep" d="M900 520 C 820 620, 720 690, 600 720 L 900 780 Z" fill="var(--plum)"/>

    <circle class="brand-disc" cx="236" cy="190" r="232" fill="var(--cream)" opacity="0.88"/>

    <path class="info-panel" d="M0 960 C 150 770, 360 680, 590 690 C 730 696, 840 740, 900 770 L 900 1200 L 0 1200 Z" fill="var(--cream)"/>

    <circle cx="243" cy="610" r="158" fill="var(--plum)"/>
    <rect x="80" y="450" width="330" height="330" fill="url(#studioTone)" clip-path="url(#studioClip)"
          role="img" aria-label="Man wearing a black EMS training suit with arms outstretched in a studio"/>

    <circle cx="530" cy="622" r="134" fill="var(--plum)"/>
    <rect x="395" y="490" width="270" height="270" fill="url(#parkTone)" clip-path="url(#parkClip)"
          role="img" aria-label="Two people in EMS suits stretching on grass in a park"/>

    <rect class="footer-band-shadow" x="0" y="1148" width="900" height="52" fill="var(--plum-deep)"/>
    <rect class="footer-band" x="0" y="1132" width="900" height="30" fill="var(--plum)"/>
  </svg>

  <div class="brand">
    <span class="brand-mark"></span>
    <span class="brand-name">Maren's Atelier</span>
  </div>

  <h1 class="headline">
    <span class="headline-kicker">Cycling training with</span>
    <span class="headline-main">Muscle electrostimulation</span>
  </h1>
  <div class="headline-rule"></div>

  <div class="body-copy">
    <p>Maren's Atelier brings you suit with muscle electrostimulation, a Bio-Jacket that can be very helpful for bike riders for the very first time in <strong>Alpenrad Pedal Days.</strong></p>
    <p>From the world leaders in manufacturing and distribution of electrostimulation equipment <strong>Pulsavo Group</strong> offers advice for the implementation of our EMS equipment along with various other services as a service inside our studio.</p>
  </div>
</main>
</body>
</html>
```